Need a stunning home page for Car rental company

For a client, I need a slick and sumber home page design. It is a small, local car rental company, with a handful of cars available for rent.
Selling points: affordable lease, availability, always clean cars
The design should be:
- flat and modern
- no, or very few animations/sliders
- CTA: booking form for renting a car.
- 3 featured cars with images and facts (see website) with button to read more about the car.
- fullscreen background video can be an option
- main colour: #efba01
The site is under construction here:
http://tavnumobil.kessvira.no/
Delivery requirements:
I need a layered & well organised PSD file delivered.

```html
<!DOCTYPE html>
<html lang="en">
<head>
<meta charset="utf-8">
<title>Tavnumobil – Car Rental</title>
<link href="https://fonts.googleapis.com/css2?family=Ubuntu:wght@400;500;700&display=swap" rel="stylesheet">
<style>
:root{
  --brand:#efba01;
  --ink:#555;
  --ink-soft:#888;
  --light:#f1f1f1;
  --line:#ddd;
  --dark:#2b2b2b;
  --btn:#4a4a4a;
}
*{box-sizing:border-box;margin:0;padding:0}
html,body{width:745px;height:1200px;overflow:hidden}
body{position:relative;font-family:'Ubuntu',sans-serif;color:var(--ink);background:#fff;border-top:2px solid #999}
.abs{position:absolute}
/* header */
.langs{left:552px;top:9px;display:flex;gap:5px}
.langs span{width:10px;height:7px;display:block}
.account{left:598px;top:0;width:60px;height:32px;background:#8a8a8a;color:#fff;font-size:8px;text-align:center;padding-top:6px;clip-path:polygon(0 0,100% 0,100% 100%,50% 80%,0 100%)}
.logo{left:88px;top:32px;font-size:22px;font-weight:700;color:var(--ink);letter-spacing:1px}
.question{left:368px;top:44px;display:flex;gap:7px;align-items:center}
.question .ic{width:20px;height:18px;background:var(--brand);border-radius:3px;display:flex;align-items:center;justify-content:center}
.question p{font-size:8px;color:var(--ink-soft);line-height:11px}
.question b{font-size:9px;color:var(--ink);font-weight:500}
.search{left:487px;top:45px;width:171px;height:22px;border:1px solid var(--line);font-size:7px;color:var(--ink-soft);padding:6px 9px}
.search svg{position:absolute;right:6px;top:5px}
/* nav */
.hero{left:0;top:105px;width:745px;height:313px;background:radial-gradient(ellipse at 25% 55%,#6b6558 0%,#2b2620 45%,#8a6a30 75%,#c9a260 100%)}
.play{left:184px;top:227px;width:46px;height:46px;border:2px solid #fff;border-radius:50%}
.play:after{content:"";position:absolute;left:17px;top:12px;border-left:14px solid #fff;border-top:9px solid transparent;border-bottom:9px solid transparent}
.dots{left:88px;top:397px;display:flex;gap:3px}
.dots span{width:12px;height:2px;background:#fff}
.dots span:first-child{background:var(--brand)}
.nav{left:87px;top:84px;width:571px;height:42px;background:var(--brand);display:flex;align-items:center;border-bottom:2px solid #d9a800}
.nav a{color:#fff;font-size:8px;font-weight:500;text-decoration:none;flex:auto;text-align:center;border-right:1px solid rgba(255,255,255,.35)}
.nav a:last-child{border:0}
/* booking */
.booking{left:422px;top:195px;width:243px;height:242px;background:#fff;border-radius:3px;box-shadow:0 8px 10px -6px rgba(0,0,0,.35);padding:14px 16px}
.booking h2{font-size:13px;color:var(--brand);font-weight:700;padding-bottom:7px;border-bottom:1px dotted var(--line);margin-bottom:12px}
.field{height:26px;border:1px solid var(--line);font-size:8px;color:var(--ink-soft);padding:8px 13px;margin-bottom:9px;position:relative}
.row{display:flex;gap:9px}
.row .field{width:99px}
.cal{position:absolute;right:8px;top:6px;width:13px;height:12px;border:1px solid #aaa}
.book-btn{width:85px;height:29px;background:var(--btn);color:#fff;font-size:10px;border-radius:4px;display:flex;align-items:center;justify-content:center;margin-top:2px}
/* welcome */
.welcome{left:0;top:460px;width:745px;text-align:center}
h3{font-size:15px;font-weight:700;color:#666}
h3 em{font-style:normal;color:var(--brand)}
.welcome p{font-size:7px;line-height:14px;color:var(--ink-soft);width:510px;margin:12px auto 0}
/* featured */
.featured{left:0;top:546px;width:745px;height:399px;background:var(--light)}
.featured h3{text-align:center;margin-top:18px}
.card{top:599px;width:176px;height:304px;background:#fff;box-shadow:0 7px 8px -5px rgba(0,0,0,.3)}
.card .img{height:101px}
.card .head{display:flex;justify-content:space-between;align-items:center;padding:10px 12px 6px}
.card .name{font-size:11px;font-weight:700;color:#555}
.price{background:var(--brand);color:#fff;font-size:10px;font-weight:700;padding:2px 4px;min-width:70px;text-align:right}
.price small{font-size:6px;font-weight:400}
.specs{padding:0 14px;font-size:7px;color:var(--ink-soft);display:grid;grid-template-columns:83px 1fr;row-gap:8.5px;margin-top:4px}
.more{margin:11px 0 0 15px;width:60px;height:21px;background:var(--btn);color:#fff;font-size:6.5px;font-weight:700;border-radius:3px;display:flex;align-items:center;justify-content:center}
/* blog */
.blog-title{left:0;top:969px;width:745px;text-align:center}
.post{top:1015px;display:flex;gap:14px;width:273px}
.thumb{width:88px;height:73px;border:3px solid #fff;box-shadow:0 0 2px rgba(0,0,0,.3);flex:none}
.meta{font-size:6px;color:var(--brand)}
.post h4{font-size:9.5px;font-weight:400;color:#444;margin:6px 0 4px;padding-bottom:5px;border-bottom:1px solid var(--line)}
.post p{font-size:6.5px;line-height:14px;color:var(--ink-soft);text-align:justify}
/* footer */
.footer{left:0;top:1130px;width:745px;height:70px;background:var(--dark);color:#fff}
.fnav{position:absolute;left:88px;top:19px;font-size:7px}
.fnav span{margin:0 5px}
.copy{position:absolute;left:88px;top:41px;font-size:7px}
.social{position:absolute;left:559px;top:25px;display:flex;gap:9px}
.social span{width:18px;height:18px;display:block}
</style>
</head>
<body>
<div class="abs langs"><span style="background:#c8102e"></span><span style="background:#1f3a7a"></span></div>
<div class="abs account">My Account</div>
<div class="abs logo">TAVNUMOBIL</div>
<div class="abs question">
  <div class="ic"><svg width="10" height="10" viewBox="0 0 10 10"><path d="M2 1l2 2-1 1.5c.7 1.3 1.2 1.8 2.5 2.5L7 6l2 2-1.5 1.5C5 9 1 5 .5 2z" fill="#fff"/></svg></div>
  <p>Question?<br><b>Call us 91234560</b></p>
</div>
<div class="abs search">Search<svg width="12" height="12" viewBox="0 0 12 12"><circle cx="5" cy="5" r="3.5" fill="none" stroke="#777"/><path d="M7.5 7.5l3.5 3.5" stroke="#777" stroke-width="1.4"/></svg></div>

<div class="abs hero" role="img" aria-label="Dark grey sports coupe speeding through a lit tunnel"></div>
<div class="abs play"></div>
<div class="abs dots"><span></span><span></span><span></span><span></span></div>

<nav class="abs nav">
  <a href="#">HOME</a><a href="#">THE FLEET OUR</a><a href="#">SERVICES</a><a href="#">CONTACT US</a><a href="#">BLOG</a><a href="#">PAGE TEMPLATES</a><a href="#">ABOUT US</a>
</nav>

<form class="abs booking">
  <h2>BOOKING FORM TO RENT A CAR</h2>
  <div class="field">Name</div>
  <div class="field">Phone</div>
  <div class="field">Email</div>
  <div class="row"><div class="field">Pickup Date<span class="cal"></span></div><div class="field" style="width:100px">Drop off Date<span class="cal"></span></div></div>
  <div class="row" style="align-items:flex-start">
    <div class="field" style="width:99px">Car Type<span style="position:absolute;right:9px;top:8px;border-top:6px solid #999;border-left:4px solid transparent;border-right:4px solid transparent"></span></div>
    <div class="book-btn" style="margin-left:12px">BOOK NOW</div>
  </div>
</form>

<section class="abs welcome">
  <h3>WELCOME TO <em>TAVNUMOBIL CAR</em></h3>
  <p>Tavnumobil is a fleet of Jørpeland and rent vans and cars for people who need a ekstrabil relocation, vacation, city tour or whatever. We beat the service, and most likely also the price. And you can trust that the car you get from us is both clean and pretty!</p>
</section>

<section class="abs featured"><h3>FEATURED <em>CARS</em></h3></section>

<article class="abs card" style="left:87px">
  <div class="img" role="img" aria-label="Silver compact van" style="background:linear-gradient(#9a9a9a,#d6d6d6)"></div>
  <div class="head"><span class="name">VAN</span><span class="price">kr 600 <small>per day</small></span></div>
  <div class="specs"><span>Biltyp to</span><span>Varebil</span><span>Maks. pers.</span><span>2</span><span>Ant. Doors</span><span>5</span><span>Min. driver age</span><span>21</span><span>Girtype</span><span>Manuell</span><span>Klima Anlegg?</span><span>Well</span><span>Unlimited km?</span><span>No</span></div>
  <div class="more">READ MORE</div>
</article>
<article class="abs card" style="left:284px">
  <div class="img" role="img" aria-label="Yellow hatchback" style="background:linear-gradient(#cfcfcf,#e8c02a 70%,#bdbdbd)"></div>
  <div class="head"><span class="name">CAR</span><span class="price">kr 800 <small>per day</small></span></div>
  <div class="specs"><span>Biltyp to</span><span>Varebil</span><span>Maks. pers.</span><span>2</span><span>Ant. Doors</span><span>5</span><span>Min. driver age</span><span>21</span><span>Girtype</span><span>Manuell</span><span>Klima Anlegg?</span><span>Well</span><span>Unlimited km?</span><span>No</span></div>
  <div class="more">READ MORE</div>
</article>
<article class="abs card" style="left:481px">
  <div class="img" role="img" aria-label="Dark brown crossover car" style="background:linear-gradient(#c4c4c4,#3a2e2a 60%,#ddd)"></div>
  <div class="head"><span class="name">KESSRA</span><span class="price"><small>per day</small></span></div>
  <div class="specs"><span>Biltyp to</span><span>Varebil</span><span>Maks. pers.</span><span>2</span><span>Ant. Doors</span><span>5</span><span>Min. driver age</span><span>21</span><span>Girtype</span><span>Manuell</span><span>Klima Anlegg?</span><span>Well</span><span>Unlimited km?</span><span>No</span></div>
  <div class="more">READ MORE</div>
</article>

<div class="abs blog-title"><h3>LATEST <em>BLOG</em></h3></div>
<article class="abs post" style="left:89px">
  <div class="thumb" role="img" aria-label="Car dashboard interior" style="background:linear-gradient(#555,#222)"></div>
  <div><div class="meta">Journal, Photography, Web Design | 9 Comments</div><h4>FERMENTUM PHARETRA TORTOR</h4><p>Fusce dapibus, tellus ac cursus commodo, tortor mauris condimentum nibh, ut fermentum massa justo sit amet.Fusce dapibus.</p></div>
</article>
<article class="abs post" style="left:386px">
  <div class="thumb" role="img" aria-label="White sedan with open doors" style="background:linear-gradient(#f2f2f2,#bbb)"></div>
  <div><div class="meta">Journal, Photography, Web Design | 9 Comments</div><h4>FERMENTUM PHARETRA TORTOR</h4><p>Fusce dapibus, tellus ac cursus commodo, tortor mauris condimentum nibh, ut fermentum massa justo sit amet.Fusce dapibus.</p></div>
</article>

<footer class="abs footer">
  <div class="fnav">HOME<span>|</span>THE FLEET OUR<span>|</span>SERVICES<span>|</span>CONTACT US<span>|</span>BLOG<span>|</span>PAGE TEMPLATES<span>|</span>ABOUT US</div>
  <div class="copy">Copyright © 2014 tavnumobil | All rights reserved</div>
  <div class="social"><span style="background:#3b5998"></span><span style="background:#1da1f2"></span><span style="background:#d8231b"></span><span style="background:#f28c1c"></span></div>
</footer>
</body>
</html>
```